Kitchen manufaturer business card/logo design

I am a small kitchen manufacturing company that makes and installs all sorts of cabinetry.

The colours im looking to incorporate in the card are light/baby blue, white and black.

Incorporate 5 stars to show quality workmanship and product.

Looking for a modern classy design.
Updates

Hey guys, New idea. The logo should be made using HK in the most modern way possible as well as the full company name below it. Thanks.

Target Market(s)

Anyone with a home thats looking for a new cabinetry of any sort.

Industry/Entity Type

Business

Contact Information for Business Card

Harbor Kitchens
Tod Villaran
PH 0431 582 904
Email- harborkitchens@mailvane.example
ABN- 73 208 561 339
-Kitchens
-Vanities
-Laundries
-Media Units
-Studies
-Wardrobes
-3D Computer Designs

Requirements
Must have

• The front of the card must only have the company name.
The different types of cabinetry I do must be on the back of the card in point form but instead of using points use stars.
Nice to have
• Just think classy and quality

```html
<!DOCTYPE html>
<html lang="en">
<head>
<meta charset="utf-8">
<title>Harbor Kitchens – Business Card</title>
<link href="https://fonts.googleapis.com/css2?family=Grand+Hotel&family=Montserrat:wght@400;500;600&display=swap" rel="stylesheet">
<style>
  :root {
    --stage: #e8e5e0;
    --card-dark: #231f20;
    --card-light: #ffffff;
    --baby-blue: #8fcfee;
    --ink: #231f20;
    --white: #ffffff;
  }
  * { margin: 0; padding: 0; box-sizing: border-box; }
  html, body {
    width: 1200px; height: 1000px; overflow: hidden;
    background: var(--stage);
  }
  .canvas { position: relative; width: 1200px; height: 1000px; }

  .card {
    position: absolute; left: 225px; width: 750px; height: 453px;
    box-shadow: 0 2px 6px rgba(0,0,0,0.25);
  }
  .card--front { top: 32px; background: var(--card-dark); }
  .card--back { top: 510px; background: var(--card-light); }

  /* Front */
  .front-name {
    position: absolute; inset: 0;
    display: flex; align-items: center; justify-content: center;
    font-family: "Montserrat", sans-serif; font-weight: 600;
    font-size: 52px; color: var(--baby-blue); letter-spacing: 1px;
  }

  /* Back: services */
  .services {
    position: absolute; left: 52px; right: 50px; top: 40px;
    font-family: "Grand Hotel", cursive; font-size: 33px; color: var(--ink);
    line-height: 60px;
  }
  .services__row { display: flex; justify-content: space-between; white-space: nowrap; }
  .services__row--short { justify-content: flex-start; gap: 16px; }
  .service__star {
    color: var(--baby-blue); font-family: "Montserrat", sans-serif;
    font-size: 20px; margin-right: 3px; vertical-align: 3px;
  }
  .rule {
    position: absolute; left: 52px; width: 647px; top: 182px;
    height: 2px; background: var(--ink);
  }

  /* Back: name block */
  .back-name {
    position: absolute; left: 40px; width: 270px; top: 215px; height: 188px;
    display: flex; align-items: center; justify-content: center; text-align: center;
    font-family: "Montserrat", sans-serif; font-weight: 600;
    font-size: 30px; line-height: 1.2; color: var(--ink);
  }
  .divider {
    position: absolute; left: 337px; top: 214px; width: 2px; height: 188px;
    background: var(--ink);
  }

  /* Back: contact */
  .contact {
    position: absolute; left: 369px; top: 212px;
    font-family: "Montserrat", sans-serif; color: var(--ink);
  }
  .contact__person {
    font-size: 27px; font-weight: 500; letter-spacing: 1.5px;
    color: var(--baby-blue); text-transform: uppercase; margin-bottom: 44px;
  }
  .contact__line { font-size: 20px; line-height: 44px; white-space: nowrap; }
  .contact__label { color: var(--baby-blue); margin-right: 4px; }
</style>
</head>
<body>
<main class="canvas">
  <section class="card card--front" aria-label="Card front">
    <div class="front-name">Harbor Kitchens</div>
  </section>

  <section class="card card--back" aria-label="Card back">
    <div class="services">
      <div class="services__row">
        <span><span class="service__star">★</span>Kitchens</span>
        <span><span class="service__star">★</span>Wardrobes</span>
        <span><span class="service__star">★</span>Vanities</span>
        <span><span class="service__star">★</span>Laundries</span>
      </div>
      <div class="services__row">
        <span><span class="service__star">★</span>Media Units</span>
        <span><span class="service__star">★</span>Studies</span>
        <span><span class="service__star">★</span>3D Computer Designs</span>
      </div>
    </div>
    <div class="rule"></div>

    <div class="back-name">Harbor Kitchens</div>
    <div class="divider"></div>

    <div class="contact">
      <p class="contact__person">Tod Villaran</p>
      <p class="contact__line"><span class="contact__label">t</span>0431 582 904</p>
      <p class="contact__line"><span class="contact__label">e</span>harborkitchens@mailvane.example</p>
      <p class="contact__line"><span class="contact__label">ABN</span>73 208 561 339</p>
    </div>
  </section>
</main>
</body>
</html>
```